We need a need two-page flyer that talks about the services of Bright Harbour. We like this created in ppt if possible (let me know if not). We have created the BH ppt for your reference. Please use the attached Oldharbour .pdf for reference. We like this to be fun and creative in flair and style. Something that the sales people can use and will wow the client if we email it to them.

```html
<!DOCTYPE html>
<html lang="en">
<head>
<meta charset="utf-8">
<title>Bright Harbour – Services Flyer</title>
<link href="https://fonts.googleapis.com/css2?family=Lato:ital,wght@0,400;0,700;0,900;1,400&display=swap" rel="stylesheet">
<style>
:root{
  --stage:#4b4b4b;
  --paper:#ffffff;
  --paper-tint:#f1f2f4;
  --red:#c9202a;
  --red-dark:#a3161e;
  --green:#3b8a2c;
  --blue:#2c3a8e;
  --purple:#3f2c8c;
  --ink:#3a3a3a;
  --ink-soft:#555;
}
*{box-sizing:border-box;margin:0;padding:0}
html,body{width:1090px;height:1200px;overflow:hidden}
body{background:var(--stage);font-family:"Lato",sans-serif;color:var(--ink);position:relative}
.page{position:absolute;top:247px;width:500px;height:706px;background:linear-gradient(160deg,var(--paper) 0%,var(--paper-tint) 100%);overflow:hidden;box-shadow:0 4px 14px rgba(0,0,0,.35)}
.page--front{left:30px}
.page--back{left:560px}
.abs{position:absolute}
.hero{position:absolute;left:0;top:0;width:500px;height:260px}
.brand{position:absolute;display:flex;align-items:center;gap:8px;font-weight:700;letter-spacing:.5px}
.brand__square{width:14px;height:14px;background:var(--red)}
.brand--hero{right:28px;top:28px;color:#fff;font-size:28px}
.brand--back{right:38px;top:630px;color:var(--ink);font-size:22px}
.title-small{font-size:19px;color:var(--red);font-weight:400;letter-spacing:.3px}
.title-big{font-size:23px;color:var(--green);font-weight:900;letter-spacing:.5px;line-height:1}
.title-sub{font-size:11px;color:var(--red);font-style:italic}
.section-head{font-size:9.5px;color:var(--green);display:flex;align-items:center;gap:5px}
.section-head::before{content:"";width:6px;height:6px;background:var(--red)}
.body-copy{font-size:6.6px;line-height:9px;color:var(--ink-soft);text-align:justify}
.body-copy + .body-copy{margin-top:7px}
.photo{position:absolute}
.band{position:absolute;left:0;top:237px;width:500px;height:26px;background:var(--red);color:#fff;font-size:18px;font-weight:700;text-align:center;line-height:26px}
.col-head{font-size:8.6px;color:var(--red);font-weight:700;border-bottom:1px solid var(--red);display:inline-block;padding-bottom:1px;margin-bottom:6px}
.ticks{list-style:none}
.ticks li{position:relative;padding-left:11px;font-size:6.4px;line-height:8.4px;color:var(--ink-soft);text-align:justify;margin-bottom:8px}
.ticks li svg{position:absolute;left:0;top:1px;width:6px;height:6px}
.collage{position:absolute;left:30px;top:447px;width:441px;height:166px;border:3px solid var(--blue);background:var(--blue);display:grid;grid-template-columns:126fr 84fr 105fr 104fr;grid-template-rows:1fr 1fr;gap:3px}
.collage__cell{border-radius:0}
.cell--party{background:linear-gradient(180deg,#9ab6d8,#c9c6b5)}
.cell--carve{background:linear-gradient(160deg,#5c4a6e,#c9c2c8)}
.cell--foliage{grid-row:1 / span 2;grid-column:2;background:linear-gradient(180deg,#3f7d2b,#8fbf52)}
.cell--lights{background:linear-gradient(160deg,#4a1f1a,#b8392e)}
.cell--booth{background:linear-gradient(180deg,#7c95b3,#a08e77)}
.cell--truck{grid-column:3 / span 2;background:linear-gradient(180deg,#8fb3dc,#d7dad6 60%,#6e8a4a)}
.footer{position:absolute;left:0;top:640px;width:500px;height:66px}
.footer__name{position:absolute;left:30px;top:649px;color:#fff;font-size:9.5px;font-weight:700}
.footer__address{position:absolute;left:20px;top:673px;color:#fff;font-size:7px;line-height:9px;display:flex;gap:4px}
.footer__phone{position:absolute;left:184px;top:677px;color:#fff;font-size:14px;display:flex;align-items:center;gap:6px}
.footer__divider{position:absolute;left:342px;top:672px;width:1px;height:26px;background:rgba(255,255,255,.6)}
.footer__web{position:absolute;left:352px;top:674px;color:#fff;font-size:7px;line-height:10px}
</style>
</head>
<body>

<!-- FRONT PAGE -->
<section class="page page--front">
  <svg class="hero" viewBox="0 0 500 260" role="img" aria-label="Photo of a hangar event venue with a vintage aircraft and long banquet tables lit in warm tones">
    <defs>
      <linearGradient id="heroShade" x1="0" y1="0" x2="0" y2="1">
        <stop offset="0" stop-color="#0c0c14"/>
        <stop offset=".55" stop-color="#4a3222"/>
        <stop offset="1" stop-color="#c9c7cc"/>
      </linearGradient>
    </defs>
    <rect x="0" y="0" width="500" height="260" fill="url(#heroShade)"/>
    <polygon points="0,140 500,238 500,260 0,260" fill="#f6f6f7"/>
    <polygon points="0,140 500,238 500,248 0,188" fill="var(--red)"/>
  </svg>
  <div class="brand brand--hero"><span class="brand__square"></span>BRIGHT HARBOUR</div>

  <div class="abs" style="left:29px;top:232px">
    <div class="title-small">EVENT MANAGEMENT</div>
    <div class="title-big">SERVICES</div>
    <div class="title-sub" style="margin-top:3px">Bringing People, Businesses, Markets and Ideas Together</div>
  </div>

  <div class="abs" style="left:29px;top:316px;width:205px">
    <div class="section-head">Themed Props and Décor</div>
    <p class="body-copy" style="margin-top:6px">At Bright Harbour we are known for providing décor that completely changes the surrounds of your venue and provides your guests with an immersive event experience. Our expert event designers understand how the product will be used and where it will be most impactful.</p>
    <p class="body-copy">Whether being transported to outer space or to a tropical paradise, our props drive each theme home. We also will use foliage, lighting, ice, and even custom décor items.</p>
  </div>

  <svg class="photo" style="left:271px;top:314px" width="192" height="94" viewBox="0 0 192 94" role="img" aria-label="Photo of a ship-themed set with a wooden wheel under teal light">
    <defs><linearGradient id="pTeal" x1="0" y1="0" x2="1" y2="1"><stop offset="0" stop-color="#0f3c52"/><stop offset="1" stop-color="#3fb2c6"/></linearGradient></defs>
    <polygon points="30,2 190,2 172,80 12,80" fill="none" stroke="var(--blue)" stroke-width="1.5"/>
    <polygon points="22,10 182,10 164,90 4,90" fill="url(#pTeal)"/>
  </svg>

  <svg class="photo" style="left:37px;top:443px" width="182" height="96" viewBox="0 0 182 96" role="img" aria-label="Photo of a room washed in magenta light with a lit dance floor">
    <defs><linearGradient id="pPink" x1="0" y1="0" x2="1" y2="1"><stop offset="0" stop-color="#5a1a7a"/><stop offset="1" stop-color="#e05ae8"/></linearGradient></defs>
    <polygon points="4,2 176,2 158,82 0,82" fill="none" stroke="var(--red)" stroke-width="1.5"/>
    <polygon points="22,12 180,12 164,94 6,94" fill="url(#pPink)"/>
  </svg>

  <div class="abs" style="left:253px;top:440px;width:207px">
    <div class="section-head">Glow Harbour</div>
    <p class="body-copy" style="margin-top:6px">Glow Harbour was born from the need to eliminate pesky cords at our events. Our lighted décor is now completely battery operated. We now sell most of our lights to multiple companies and theme parks throughout the United States.</p>
    <p class="body-copy">Our lighted products are brand friendly, meaning we can add a logo or monogram to just about any of our lighted décor items.</p>
  </div>

  <div class="abs" style="left:29px;top:557px;width:205px">
    <div class="section-head">Green Harbour</div>
    <p class="body-copy" style="margin-top:6px">Green Harbour is our only company that is not located on property. We have 40,000 square feet of green houses with a large selection of inventory from 14' Amstel Ficus Trees, 12' Palms, to lush Boston Ferns and many more in between.</p>
  </div>

  <svg class="photo" style="left:271px;top:539px" width="192" height="94" viewBox="0 0 192 94" role="img" aria-label="Photo of carved tiki statues among tropical foliage">
    <defs><linearGradient id="pGreen" x1="0" y1="0" x2="1" y2="1"><stop offset="0" stop-color="#2e5a22"/><stop offset="1" stop-color="#9cc865"/></linearGradient></defs>
    <polygon points="30,2 190,2 172,80 12,80" fill="none" stroke="var(--green)" stroke-width="1.5"/>
    <polygon points="22,10 182,10 164,90 4,90" fill="url(#pGreen)"/>
  </svg>

  <svg class="footer" viewBox="0 0 500 66" aria-hidden="true">
    <polygon points="0,0 140,0 172,22 500,22 500,66 0,66" fill="var(--red)"/>
    <polygon points="140,0 172,22 500,22 500,24 170,24" fill="var(--red-dark)"/>
  </svg>
  <div class="footer__name">Bright Harbour</div>
  <div class="footer__address">
    <svg width="8" height="10" viewBox="0 0 8 10"><path d="M4 0a3.3 3.3 0 0 1 3.3 3.3C7.3 6 4 9.5 4 9.5S.7 6 .7 3.3A3.3 3.3 0 0 1 4 0z" fill="none" stroke="#fff" stroke-width=".9"/><circle cx="4" cy="3.3" r="1.1" fill="#fff"/></svg>
    <span>120 Quayside Lane,<br>Lakeport, FL 30000</span>
  </div>
  <div class="footer__phone">
    <svg width="14" height="14" viewBox="0 0 14 14"><circle cx="7" cy="7" r="6.3" fill="none" stroke="#fff" stroke-width="1"/><path d="M4.6 3.8l1.3 1.5-.7.9c.5 1 1.3 1.8 2.3 2.3l.9-.7 1.5 1.3-.8 1.1C6.8 10 4 7.2 3.6 4.6z" fill="#fff"/></svg>
    (555) 010-4821
  </div>
  <div class="footer__divider"></div>
  <div class="footer__web">✉ info@brightharbour.example<br>● www.brightharbour.example</div>
</section>

<!-- BACK PAGE -->
<section class="page page--back">
  <div class="abs" style="left:30px;top:26px;width:234px">
    <div class="section-head">Carving Ice</div>
    <p class="body-copy" style="margin-top:6px">Ice sculptures are a central point and unique statement at a corporate event or wedding. Ice will attract attention and provide a memorable focal and visual for attendee discussion. It can even be an interactive experience when your guests use an ice luge for the first time or drink from a glass with a large ice cube featuring your logo!</p>
  </div>

  <svg class="photo" style="left:273px;top:22px" width="192" height="94" viewBox="0 0 192 94" role="img" aria-label="Photo of a server pouring a drink through an ice luge">
    <defs><linearGradient id="pIce" x1="0" y1="0" x2="1" y2="1"><stop offset="0" stop-color="#3a2e48"/><stop offset="1" stop-color="#cfd4de"/></linearGradient></defs>
    <polygon points="30,2 190,2 172,80 12,80" fill="none" stroke="var(--green)" stroke-width="1.5"/>
    <polygon points="22,10 182,10 164,90 4,90" fill="url(#pIce)"/>
  </svg>

  <svg class="photo" style="left:35px;top:127px" width="182" height="96" viewBox="0 0 182 96" role="img" aria-label="Photo of a trade show booth with lit furniture and string lights">
    <defs><linearGradient id="pBooth" x1="0" y1="0" x2="1" y2="1"><stop offset="0" stop-color="#1e2e3c"/><stop offset="1" stop-color="#7aa4c4"/></linearGradient></defs>
    <polygon points="4,2 176,2 158,82 0,82" fill="none" stroke="var(--blue)" stroke-width="1.5"/>
    <polygon points="22,12 180,12 164,94 6,94" fill="url(#pBooth)"/>
  </svg>

  <div class="abs" style="left:253px;top:128px;width:210px">
    <div class="section-head">Custom Fabrication for All Types of Events</div>
    <p class="body-copy" style="margin-top:6px">At Bright Harbour our in-house fabrication team has the ability to deliver custom designs and fabrications that will make your next event a unique one. Our team of professionals specializes in providing creative event solutions for companies planning both in-office and off-site activities. Our services provide the very best in custom staging, furniture and décor, scenic displays, tradeshow booths, and much more.</p>
  </div>

  <div class="band">Our Approach to a Successful Event</div>

  <div class="abs" style="left:30px;top:272px;width:210px">
    <div class="col-head">An Extension of Your Own team</div>
    <ul class="ticks">
      <li><svg viewBox="0 0 6 6"><circle cx="3" cy="3" r="2.6" fill="none" stroke="var(--red)" stroke-width=".7"/><path d="M1.7 3l.9.9L4.4 2" fill="none" stroke="var(--red)" stroke-width=".7"/></svg>When you employ Bright Harbour to create or manage one of your events, you can be assured that you are in the safe hands of thoroughbred event organizers.</li>
      <li><svg viewBox="0 0 6 6"><circle cx="3" cy="3" r="2.6" fill="none" stroke="var(--red)" stroke-width=".7"/><path d="M1.7 3l.9.9L4.4 2" fill="none" stroke="var(--red)" stroke-width=".7"/></svg>We like to work as an extension of your own company, treating your events and brands as respectfully as we do our own and consulting carefully on all significant decisions.</li>
      <li><svg viewBox="0 0 6 6"><circle cx="3" cy="3" r="2.6" fill="none" stroke="var(--red)" stroke-width=".7"/><path d="M1.7 3l.9.9L4.4 2" fill="none" stroke="var(--red)" stroke-width=".7"/></svg>We have a strong understanding of budget constraints, constantly monitoring expenditure commitments and managing the various risks involved.</li>
      <li><svg viewBox="0 0 6 6"><circle cx="3" cy="3" r="2.6" fill="none" stroke="var(--red)" stroke-width=".7"/><path d="M1.7 3l.9.9L4.4 2" fill="none" stroke="var(--red)" stroke-width=".7"/></svg>We use our extensive supplier and venue relationships to keep your costs low whilst ensuring the highest quality, with many clients finding that using our services is more cost-effective than running their events through an in-house team.</li>
    </ul>
  </div>

  <div class="abs" style="left:259px;top:272px;width:212px">
    <div class="col-head">Budget transparency</div>
    <ul class="ticks">
      <li><svg viewBox="0 0 6 6"><circle cx="3" cy="3" r="2.6" fill="none" stroke="var(--red)" stroke-width=".7"/><path d="M1.7 3l.9.9L4.4 2" fill="none" stroke="var(--red)" stroke-width=".7"/></svg>We always work to a pre-agreed budget and a pre-agreed management fee, based on the amount of sales, marketing and logistical time needed to manage your event.</li>
      <li><svg viewBox="0 0 6 6"><circle cx="3" cy="3" r="2.6" fill="none" stroke="var(--red)" stroke-width=".7"/><path d="M1.7 3l.9.9L4.4 2" fill="none" stroke="var(--red)" stroke-width=".7"/></svg>Your final bill will not differ from this pre-agreed amount unless there have been significant changes to the project along the way.</li>
    </ul>
    <div class="col-head" style="margin-top:6px">Meet the team</div>
    <ul class="ticks">
      <li><svg viewBox="0 0 6 6"><circle cx="3" cy="3" r="2.6" fill="none" stroke="var(--red)" stroke-width=".7"/><path d="M1.7 3l.9.9L4.4 2" fill="none" stroke="var(--red)" stroke-width=".7"/></svg>Organizing professional events requires a significant amount of time and 'attention-to-detail' across a whole range of different disciplines – but we endeavor to provide a single point of contact to streamline client communications wherever possible.</li>
    </ul>
  </div>

  <div class="collage">
    <div class="collage__cell cell--party" role="img" aria-label="Photo of an outdoor party with tables and colourful bunting"></div>
    <div class="collage__cell cell--foliage" role="img" aria-label="Photo of a carved tiki statue among palms"></div>
    <div class="collage__cell cell--lights" role="img" aria-label="Photo of a banquet room with lit white trees"></div>
    <div class="collage__cell cell--booth" role="img" aria-label="Photo of a stone-look themed bar booth"></div>
    <div class="collage__cell cell--carve" role="img" aria-label="Photo of an ice luge being served at an event"></div>
    <div class="collage__cell cell--truck" role="img" aria-label="Photo of a company delivery truck parked outdoors"></div>
  </div>

  <div class="brand brand--back"><span class="brand__square"></span>BRIGHT HARBOUR</div>

  <svg class="footer" viewBox="0 0 500 66" aria-hidden="true">
    <polygon points="0,0 140,0 172,22 500,22 500,66 0,66" fill="var(--red)"/>
    <polygon points="140,0 172,22 500,22 500,24 170,24" fill="var(--red-dark)"/>
  </svg>
  <div class="footer__name">Bright Harbour</div>
  <div class="footer__address">
    <svg width="8" height="10" viewBox="0 0 8 10"><path d="M4 0a3.3 3.3 0 0 1 3.3 3.3C7.3 6 4 9.5 4 9.5S.7 6 .7 3.3A3.3 3.3 0 0 1 4 0z" fill="none" stroke="#fff" stroke-width=".9"/><circle cx="4" cy="3.3" r="1.1" fill="#fff"/></svg>
    <span>120 Quayside Lane,<br>Lakeport, FL 30000</span>
  </div>
  <div class="footer__phone">
    <svg width="14" height="14" viewBox="0 0 14 14"><circle cx="7" cy="7" r="6.3" fill="none" stroke="#fff" stroke-width="1"/><path d="M4.6 3.8l1.3 1.5-.7.9c.5 1 1.3 1.8 2.3 2.3l.9-.7 1.5 1.3-.8 1.1C6.8 10 4 7.2 3.6 4.6z" fill="#fff"/></svg>
    (555) 010-4821
  </div>
  <div class="footer__divider"></div>
  <div class="footer__web">✉ info@brightharbour.example<br>● www.brightharbour.example</div>
</section>

</body>
</html>
```